KORVa: AI driven decarbonization application

We are seeking an engaging, user-friendly, and visually appealing user interface for our B2B SaaS platform, Brelmont KORVa. This solution helps large organizations achieve net-zero emissions using AI-driven forecasting, AI models, a emission mitigation library, and a scenario simulator..

A big challenge is to allow the user to work efficiently with multidimensional data.

Requirements:

* Design a modern, professional, and visually striking user interface, catering to a diverse audience within large corporations, including executives, strategists, and environmental specialists.

* Construct an intuitive navigation system, allowing users to seamlessly access functionalities for informed decision-making and tracking progress towards net-zero emissions.

* The application is expected to be used on desktops first

* Incorporate our brand's colors, and visual elements into the design to maintain consistency throughout the application.

* Provide design assets and documentation, such as style guides, design specifications, and necessary assets (e.g., icons, illustrations) for our development team to implement the design. We use Figma and would appreciate delivery as figma files.

Please note that we also need more pages over time. The most important is to get the work bench page right. We will also need:
* a landing page where the users can select previous scenarios and see some high level data.
* A page with information on historical data per asset
* An analytics page
* User and system administration pages.
These pages are out of scope for this project, but they should be available in the navigation solution.

Please submit your initial design concepts, accompanied by a brief explanation of your approach and the rationale behind your design choices. We will offer feedback and collaborate with the chosen designer to refine the design, ensuring it meets our requirements and vision.

We are really hoping to see some elegant user interfaces. The functionality describe in the attachment is important, but the layout is not. Feel free to invent.

Attached files:

Target Market(s)

Energy intensive industries

Requirements
Must have
• Easy to navigate through the different data dimensions: Time, assets, mitigation measures, and advanced details under mitigation measures. The design in the attached files are just our working drafts. Creative alternatives are very welcome.
Nice to have
• Elegant layouts that differ from our working drafts.

```html
<!DOCTYPE html>
<html lang="en">
<head>
<meta charset="utf-8">
<title>Brelmont KORVa – Workbench</title>
<link href="https://fonts.googleapis.com/css2?family=Montserrat:wght@400;500;600&display=swap" rel="stylesheet">
<style>
:root{
  --header:#22546c;
  --sidebar:#3b4a51;
  --side-text:#c9d6dc;
  --side-active:#2fc6d6;
  --teal-a:#1fb8c0;
  --teal-b:#0a6f78;
  --chart-bg:#1a6fb0;
  --chart-bg2:#2aa3e0;
  --timeline:#1fa6de;
  --row:#08a5e0;
  --yellow:#fdf97a;
  --pink:#ff5f83;
  --green:#4fd28a;
  --cyan:#4cf7f4;
  --peri:#7fa3ef;
  --navy:#0c6aa8;
  --accent:#4ce8f0;
  --white:#ffffff;
  --toggle:#2d5468;
}
*{box-sizing:border-box;margin:0;padding:0}
html,body{width:1200px;height:670px;overflow:hidden}
body{font-family:"Montserrat",sans-serif;color:var(--white);background:var(--sidebar);position:relative}
h2,h3{font-weight:400}
.abs{position:absolute}
.app-header{left:0;top:0;width:1200px;height:63px;background:linear-gradient(90deg,#1f5a72,#2a5a74 60%,#2a566e)}
.brand{left:14px;top:18px;font-size:24px;font-weight:500;letter-spacing:2px;display:flex;align-items:center;gap:8px}
.brand-dot{width:10px;height:10px;border-radius:50%;background:var(--white)}
.sidebar{left:0;top:63px;width:155px;height:607px;background:var(--sidebar)}
.search{left:5px;top:12px;width:143px;height:17px;border:1px solid var(--side-active);border-radius:2px}
.search svg{position:absolute;right:4px;top:3px}
.nav{position:absolute;top:52px;left:0;width:155px;list-style:none;font-size:9px;color:var(--side-text)}
.nav li{height:18.75px;line-height:18.75px;white-space:nowrap}
.nav .group{padding-left:18px;position:relative}
.nav .group::before{content:"";position:absolute;left:8px;top:7px;width:4px;height:4px;border-right:1px solid var(--side-text);border-bottom:1px solid var(--side-text);transform:rotate(-45deg)}
.nav .group.open::before{transform:rotate(45deg);top:5px}
.nav .sub{padding-left:28px;position:relative}
.nav .sub::before{content:"";position:absolute;left:21px;top:0;height:100%;border-left:1px solid #56666d}
.nav .active{background:var(--side-active);color:#1e4a58}
.panel-measure{left:155px;top:63px;width:515px;height:295px;background:linear-gradient(110deg,var(--teal-a) 0%,#139ca5 45%,var(--teal-b) 100%)}
.panel-chart{left:670px;top:63px;width:530px;height:295px;background:linear-gradient(90deg,var(--chart-bg),var(--chart-bg2))}
.panel-title{font-size:15px;text-align:center;position:absolute;top:12px;width:100%}
.sub-title{font-size:11px;position:absolute;top:48px}
.t{position:absolute;white-space:nowrap}
.th{font-size:9px;top:76px}
.tsub{font-size:5.8px;top:89px}
.row-cell{font-size:7.5px}
.toggle{position:absolute;width:13px;height:13px;border-radius:3px;background:var(--toggle)}
.toggle.on{background:var(--white)}
.param-label{font-size:9px;left:356px}
.param-input{position:absolute;left:414px;width:77px;height:14px;background:var(--white);color:#1a6a78;border-radius:2px;font-size:7.5px;text-align:center;line-height:14px}
.timeline{left:155px;top:358px;width:1045px;height:242px;background:var(--timeline)}
.tl-title{left:0;width:1045px;text-align:center;top:10px;font-size:15px;position:absolute}
.ctrl{position:absolute;top:34px;width:23px;height:22px;background:var(--white);border-radius:3px;display:flex;align-items:center;justify-content:center}
.date-select{position:absolute;left:104px;top:34px;width:89px;height:22px;background:var(--accent);border-radius:3px;font-size:8.5px;line-height:22px;padding-left:8px}
.date-select::after{content:"";position:absolute;right:9px;top:8px;border:4px solid transparent;border-top:6px solid var(--white)}
.lane{position:absolute;left:3px;width:1038px;height:27px;background:var(--row)}
.bar{position:absolute;height:23px;padding:3px 0 0 12px;font-size:8.5px;line-height:1.1}
.bar small{display:block;font-size:5.5px}
.bar .handle{position:absolute;right:6px;top:3px;width:17px;height:17px;border-radius:2px;background:rgba(255,255,255,.55)}
.overview{left:155px;top:600px;width:1045px;height:70px;background:linear-gradient(180deg,#1fb6de,#45e0ee)}
</style>
</head>
<body>
<header class="abs app-header">
  <div class="abs brand"><span class="brand-dot"></span>Brelmont</div>
</header>

<aside class="abs sidebar">
  <div class="abs search">
    <svg width="10" height="10" viewBox="0 0 10 10"><circle cx="4" cy="4" r="3" fill="none" stroke="#2fc6d6" stroke-width="1.2"/><line x1="6.2" y1="6.2" x2="9.5" y2="9.5" stroke="#2fc6d6" stroke-width="1.4"/></svg>
  </div>
  <ul class="nav">
    <li class="group">Switch Energy Carrier</li>
    <li class="group open">Energy efficience measures</li>
    <li class="sub">Venting to flare</li>
    <li class="sub">Venting to production</li>
    <li class="sub">Fugitive emission measure</li>
    <li class="sub active">Compressor replacement</li>
    <li class="sub">Reduced water injection</li>
    <li class="sub">Reduced gas injection</li>
    <li class="sub">Drilling improveents</li>
    <li class="group">End of pipe measures</li>
    <li class="group open">Compray structure</li>
    <li class="sub">Change end of life</li>
    <li class="sub">New net zero assets</li>
    <li class="sub">Update license ownerships</li>
    <li class="group">Logistics</li>
    <li class="group">Carbon offsets</li>
  </ul>
</aside>

<section class="abs panel-measure">
  <h2 class="panel-title">Power from shore</h2>
  <h3 class="sub-title" style="left:154px">Assets</h3>
  <h3 class="sub-title" style="left:377px">Parameters</h3>

  <span class="t th" style="left:12px">Active filters:</span>
  <span class="t th" style="left:79px">Name</span>
  <span class="t th" style="left:146px">Ownership</span>
  <span class="t th" style="left:230px">Status</span>
  <span class="t tsub" style="left:13px">Lorem</span>
  <span class="t tsub" style="left:79px">Type</span>
  <span class="t tsub" style="left:110px">Country</span>
  <span class="t tsub" style="left:146px">Title</span>
  <span class="t tsub" style="left:230px">Percent</span>
  <span class="t tsub" style="left:279px">Status</span>

  <div class="assets-rows">
    <div class="t row-cell" style="left:12px;top:108px">DEVG PVL D-5</div><div class="t row-cell" style="left:80px;top:108px">Field</div><div class="t row-cell" style="left:118px;top:108px">UK</div><div class="t row-cell" style="left:147px;top:108px">Vicont of Shetland</div><div class="t row-cell" style="left:231px;top:108px">100%</div><div class="t row-cell" style="left:260px;top:108px">Producing</div><span class="toggle" style="left:306px;top:107px"></span>
    <div class="t row-cell" style="left:12px;top:127px">DEVG PVL D-5</div><div class="t row-cell" style="left:80px;top:127px">Field</div><div class="t row-cell" style="left:118px;top:127px">UK</div><div class="t row-cell" style="left:147px;top:127px">Vicont of Shetland</div><div class="t row-cell" style="left:231px;top:127px">100%</div><div class="t row-cell" style="left:260px;top:127px">Producing</div><span class="toggle" style="left:306px;top:126px"></span>
    <div class="t row-cell" style="left:12px;top:146px">DEVG PVL D-5</div><div class="t row-cell" style="left:80px;top:146px">Field</div><div class="t row-cell" style="left:118px;top:146px">UK</div><div class="t row-cell" style="left:147px;top:146px">Vicont of Shetland</div><div class="t row-cell" style="left:231px;top:146px">100%</div><div class="t row-cell" style="left:260px;top:146px">Producing</div><span class="toggle" style="left:306px;top:145px"></span>
    <div class="t row-cell" style="left:12px;top:165px">DEVG PVL D-5</div><div class="t row-cell" style="left:80px;top:165px">Field</div><div class="t row-cell" style="left:118px;top:165px">UK</div><div class="t row-cell" style="left:147px;top:165px">Vicont of Shetland</div><div class="t row-cell" style="left:231px;top:165px">100%</div><div class="t row-cell" style="left:260px;top:165px">Producing</div><span class="toggle" style="left:306px;top:164px"></span>
    <div class="t row-cell" style="left:12px;top:184px">DEVG PVL D-5</div><div class="t row-cell" style="left:80px;top:184px">Field</div><div class="t row-cell" style="left:118px;top:184px">UK</div><div class="t row-cell" style="left:147px;top:184px">Vicont of Shetland</div><div class="t row-cell" style="left:231px;top:184px">100%</div><div class="t row-cell" style="left:260px;top:184px">Producing</div><span class="toggle" style="left:306px;top:183px"></span>
    <div class="t row-cell" style="left:12px;top:203px">DEVG PVL D-5</div><div class="t row-cell" style="left:80px;top:203px">Field</div><div class="t row-cell" style="left:118px;top:203px">UK</div><div class="t row-cell" style="left:147px;top:203px">Vicont of Shetland</div><div class="t row-cell" style="left:231px;top:203px">100%</div><div class="t row-cell" style="left:260px;top:203px">Producing</div><span class="toggle on" style="left:306px;top:202px"></span>
    <div class="t row-cell" style="left:12px;top:222px">DEVG PVL D-5</div><div class="t row-cell" style="left:80px;top:222px">Field</div><div class="t row-cell" style="left:118px;top:222px">UK</div><div class="t row-cell" style="left:147px;top:222px">Vicont of Shetland</div><div class="t row-cell" style="left:231px;top:222px">100%</div><div class="t row-cell" style="left:260px;top:222px">Producing</div><span class="toggle on" style="left:306px;top:221px"></span>
    <div class="t row-cell" style="left:12px;top:241px">DEVG PVL D-5</div><div class="t row-cell" style="left:80px;top:241px">Field</div><div class="t row-cell" style="left:118px;top:241px">UK</div><div class="t row-cell" style="left:147px;top:241px">Vicont of Shetland</div><div class="t row-cell" style="left:231px;top:241px">100%</div><div class="t row-cell" style="left:260px;top:241px">Producing</div><span class="toggle on" style="left:306px;top:240px"></span>
    <div class="t row-cell" style="left:12px;top:260px">DEVG PVL D-5</div><div class="t row-cell" style="left:80px;top:260px">Field</div><div class="t row-cell" style="left:118px;top:260px">UK</div><div class="t row-cell" style="left:147px;top:260px">Vicont of Shetland</div><div class="t row-cell" style="left:231px;top:260px">100%</div><div class="t row-cell" style="left:260px;top:260px">Producing</div><span class="toggle" style="left:306px;top:259px"></span>
  </div>

  <span class="t param-label" style="top:77px">Start</span>
  <span class="t param-label" style="top:96px">End</span>
  <span class="t param-label" style="top:114px">Duration</span>
  <span class="t param-label" style="top:133px">Factor</span>
  <span class="t param-label" style="top:152px">Jalla Jalla</span>
  <div class="param-input" style="top:69px">January 2023</div>
  <div class="param-input" style="top:88px">October 2024</div>
  <div class="param-input" style="top:107px">21 months</div>
  <div class="param-input" style="top:125px">2 x</div>
  <span class="toggle" style="left:445px;top:144px"></span>
</section>

<section class="abs panel-chart">
  <h2 class="panel-title">Predicted specific CO<sub style="font-size:9px">2</sub> emissions</h2>
  <svg class="abs" style="left:0;top:0" width="530" height="295" viewBox="670 63 530 295" font-family="Montserrat, sans-serif" font-size="8.5" fill="#9ec4ee">
    <rect x="719" y="128" width="220" height="193" fill="#80aaf2"/>
    <rect x="939" y="128" width="223" height="193" fill="#6f9ae6"/>
    <g text-anchor="end" fill="#7fb0ea">
      <text x="714" y="133">175</text><text x="714" y="160">150</text><text x="714" y="187">125</text>
      <text x="714" y="215">100</text><text x="714" y="242">75</text><text x="714" y="269">50</text>
      <text x="714" y="297">25</text><text x="714" y="324">0</text>
    </g>
    <g text-anchor="middle" fill="#7fb0ea">
      <text x="728" y="333">1995</text><text x="765" y="333">2000</text><text x="804" y="333">2005</text>
      <text x="841" y="333">2010</text><text x="880" y="333">2015</text><text x="916" y="333">2020</text>
      <text x="957" y="333">2025</text><text x="996" y="333">2030</text><text x="1036" y="333">2035</text>
      <text x="1075" y="333">2040</text><text x="1114" y="333">2045</text><text x="1150" y="333">2050</text>
    </g>
    <path d="M922,234 C960,262 1000,278 1040,287 S1110,302 1159,309" fill="none" stroke="#2fc6b8" stroke-width="1.5"/>
    <polyline fill="none" stroke="#ff79a6" stroke-width="1.5" points="941,241 966,241 976,256 984,266 994,256 1006,266 1025,263 1038,272 1050,281 1062,288 1075,291 1088,293 1100,297 1113,306 1125,308 1138,305 1159,309"/>
    <polyline fill="none" stroke="#f6f77a" stroke-width="1.5" points="722,288 726,300 730,306 734,296 739,250 742,304 746,292 750,309 754,296 758,303 762,292 766,305 769,308 772,296 775,269 779,274 784,262 788,271 792,258 796,266 800,250 804,262 808,256 812,266 816,231 820,258 824,252 828,262 832,250 836,258 838,256 842,246 846,254 850,236 853,234 857,246 861,228 864,240 869,203 872,236 875,212 878,183 881,250 884,226 888,225 891,246 894,236 897,250 900,228 903,244 906,234 909,252 912,236 915,248 918,238 922,254 926,244 930,252 934,240 938,250 942,226 946,244 952,246 960,240 969,244 978,240 990,236 1000,234 1012,232 1022,230 1031,228 1038,226 1044,220 1050,232 1056,222 1063,213 1069,200 1075,188 1082,178 1088,172 1094,170 1100,180 1106,181 1112,178 1118,174 1125,169 1132,160 1138,152 1144,144 1150,138 1155,134 1159,131"/>
    <g font-size="9">
      <line x1="720" y1="346" x2="745" y2="346" stroke="#f6f77a"/><circle cx="732" cy="346" r="3" fill="#f6f77a"/>
      <text x="750" y="349">Corporate average</text>
      <line x1="852" y1="346" x2="877" y2="346" stroke="#2fc6b8"/><circle cx="864" cy="346" r="3" fill="#2fc6b8"/>
      <text x="882" y="349">Corporate goals</text>
      <line x1="983" y1="346" x2="1008" y2="346" stroke="#ff79a6"/><circle cx="995" cy="346" r="3" fill="#ff79a6"/>
      <text x="1013" y="349">Corporate average incl measures</text>
    </g>
  </svg>
</section>

<section class="abs timeline">
  <h2 class="tl-title">Power from shore</h2>
  <span class="t" style="left:876px;top:15px;font-size:9px">7/10 Assets included</span>
  <div class="ctrl" style="left:985px;top:7px;background:var(--accent)">
    <svg width="12" height="14" viewBox="0 0 12 14"><path d="M6 1v12M2 7h8M4 3l2-2 2 2M4 11l2 2 2-2" stroke="#fff" fill="none"/></svg>
  </div>
  <div class="ctrl" style="left:14px"><svg width="16" height="10" viewBox="0 0 16 10"><path d="M8 0v10L0 5zM16 0v10L8 5z" fill="#4ce8f0"/></svg></div>
  <div class="ctrl" style="left:44px"><svg width="10" height="10" viewBox="0 0 10 10"><path d="M1 0v10l8-5z" fill="#4ce8f0"/></svg></div>
  <div class="ctrl" style="left:74px"><svg width="16" height="10" viewBox="0 0 16 10"><path d="M0 0v10l8-5zM8 0v10l8-5z" fill="#4ce8f0"/></svg></div>
  <div class="date-select">January 2023</div>

  <svg class="abs" style="left:0;top:0" width="1045" height="242" viewBox="155 358 1045 242" font-family="Montserrat, sans-serif" font-size="8.5" fill="#fff">
    <g text-anchor="middle">
      <text x="421" y="402">January 2023</text><text x="511" y="402">July 2023</text><text x="587" y="402">January 2024</text>
      <text x="678" y="402">July 2024</text><text x="751" y="402">January 2025</text><text x="842" y="402">July 2025</text>
      <text x="918" y="402">January 2026</text><text x="1009" y="402">July 2026</text><text x="1084" y="402">January 2027</text>
      <text x="1172" y="402">July 2027</text>
    </g>
    <line x1="354" y1="412" x2="1180" y2="412" stroke="#fff"/>
    <path stroke="#fff" d="M354 405v7M437 405v7M520 405v7M602 405v7M685 405v7M768 405v7M850 405v7M933 405v7M1016 405v7M1098 405v7M1180 405v7"/>
    <path stroke="#fff" d="M368 409v3M382 409v3M396 409v3M409 409v3M423 409v3M451 409v3M465 409v3M478 409v3M492 409v3M506 409v3M534 409v3M547 409v3M561 409v3M575 409v3M589 409v3M616 409v3M630 409v3M644 409v3M657 409v3M671 409v3M699 409v3M713 409v3M726 409v3M740 409v3M754 409v3M782 409v3M795 409v3M809 409v3M823 409v3M837 409v3M864 409v3M878 409v3M892 409v3M905 409v3M919 409v3M947 409v3M961 409v3M974 409v3M988 409v3M1002 409v3M1030 409v3M1043 409v3M1057 409v3M1071 409v3M1085 409v3M1112 409v3M1126 409v3M1139 409v3M1153 409v3M1167 409v3"/>
  </svg>

  <div class="lane" style="top:63px"></div>
  <div class="lane" style="top:92px"></div>
  <div class="lane" style="top:121px"></div>
  <div class="lane" style="top:150px"></div>
  <div class="lane" style="top:179px"></div>
  <div class="lane" style="top:208px"></div>

  <div class="bar" style="left:522px;width:290px;top:65px;background:var(--green)">Compressor rebundling<small>3/10 Assets included</small><span class="handle"></span></div>
  <div class="bar" style="left:331px;width:391px;top:94px;background:var(--yellow);color:#18a6dc">Optimize gas lift<small>5/10 Assets included</small><span class="handle"></span></div>
  <div class="bar" style="left:331px;width:391px;top:124px;background:var(--pink)">Power from shore<small>7/10 Assets included</small><span class="handle"></span></div>
  <div class="bar" style="left:414px;width:391px;top:153px;background:var(--cyan)">Reduced flaring<small>1/10 Assets included</small><span class="handle"></span></div>
  <div class="bar" style="left:316px;width:391px;top:182px;background:var(--peri)">Reduced flaring<small>1/10 Assets included</small><span class="handle"></span></div>
  <div class="bar" style="left:316px;width:391px;top:211px;background:var(--navy)">Reduced flaring<small>1/10 Assets included</small><span class="handle"></span></div>

  <div class="abs" style="left:281px;top:20px;width:1px;height:218px;background:var(--yellow)"></div>
  <div class="abs" style="left:274px;top:11px;width:15px;height:15px;border-radius:50%;background:var(--yellow)"></div>
</section>

<section class="abs overview">
  <svg width="1045" height="70" viewBox="0 0 1045 70">
    <path d="M0 70 L5 60 12 50 22 48 35 52 50 45 65 50 80 47 100 50 120 44 140 48 160 45 180 49 200 43 220 47 240 44 260 48 280 42 300 46 320 43 340 48 360 42 380 46 400 41 420 45 440 42 460 47 480 43 500 46 520 41 540 45 560 42 580 46 600 43 620 47 640 42 660 45 680 41 700 44 720 42 740 46 760 43 780 47 800 44 820 46 840 42 860 45 880 44 900 47 920 43 940 46 960 42 980 45 1000 44 1020 48 1045 40 L1045 70Z" fill="#1a8fd0"/>
    <rect x="334" y="0" width="428" height="70" fill="rgba(120,160,240,.35)"/>
    <rect x="330" y="22" width="8" height="20" rx="2" fill="#8fa6ec"/>
    <rect x="758" y="22" width="8" height="20" rx="2" fill="#8fa6ec"/>
  </svg>
</section>
</body>
</html>
```